-Photo booth rental Web Design Project

Our business is a small photo booth rental service serving the capital region and surrounding areas. The photo booth is a portable booth that fits up to 10 guest. I am looking for a website that will have social media capabilities and also private log ins for clients to view their photo albums online after their event. We provide full service photo booth rentals for all types of parties. I am looking for something fun and unique but also professional and I am also looking to maybe somehow incorporate the age of the photo booth which was invented in 1888. I do not have the photos of our photo booth available because we are just starting up and I wanted to get everything together first but I will provide stock photo booth pictures .Thank you for your patience i know it wont be an easy task with out those things. I added a word document describing information i will need on our website, i am looking for a home page, contact us and book an event page, online gallery page, and pricing. If you need any more information please feel free to contact me. Thanks for your help and I look forward to working with you.

Target Market(s)

For everyone from brides to be for their weddings or private parties, corporate parties, school dances, charity events, community events ect

Industry/Entity Type

Business

Requirements
Nice to have
• social media sharing

```html
<!DOCTYPE html>
<html lang="en">
<head>
<meta charset="utf-8">
<title>Giggle Frames Photo Booth</title>
<link href="https://fonts.googleapis.com/css2?family=Open+Sans:ital,wght@0,400;0,600;0,700;0,800;1,400;1,600&family=Oswald:wght@500;700&display=swap" rel="stylesheet">
<style>
:root{
  --ink:#2e1d14;
  --brown-dark:#3b2219;
  --brown-deep:#2a170f;
  --tan:#a58e70;
  --tan-light:#c9b79b;
  --tan-text:#8f7656;
  --grey-text:#777069;
  --rule:#b7aca6;
  --card-border:#e2ddd8;
  --card-bg:#fbfaf9;
  --ribbon:#d65a9d;
  --badge:#1e2232;
  --slider-btn:#c8432f;
  --white:#ffffff;
}
*{box-sizing:border-box;margin:0;padding:0}
html,body{width:1200px;height:2582px;overflow:hidden;background:var(--white)}
body{position:relative;font-family:"Open Sans",Arial,sans-serif;color:var(--ink)}
.abs{position:absolute}

/* header */
.brand{left:0;width:1200px;top:38px;text-align:center;font-family:"Open Sans",Arial,sans-serif;font-weight:700;font-size:46px;letter-spacing:-1px;color:var(--brown-dark);display:flex;justify-content:center;align-items:center;gap:14px}
.brand-dot{width:22px;height:22px;border-radius:50%;background:var(--brown-dark)}
.double-rule{left:171px;width:854px;height:5px;border-top:2px solid var(--rule);border-bottom:1px solid var(--rule)}
.main-nav{left:171px;width:854px;top:143px;display:flex;justify-content:center;align-items:center;font-size:11px;text-transform:uppercase;color:var(--ink);gap:22px}
.main-nav .line{width:120px;height:1px;background:var(--ink)}
.main-nav .sep{color:var(--ink)}

/* hero */
.hero{left:171px;top:194px;width:854px;height:502px;overflow:hidden}
.hero-photo-family{left:0;top:0;width:427px;height:502px;background:linear-gradient(135deg,#f4f1ee 0%,#e9d8cc 35%,#c96a45 65%,#d8553d 100%)}
.hero-photo-bike{left:427px;top:0;width:427px;height:502px;background:linear-gradient(160deg,#6b5a2a 0%,#a2862f 35%,#7a6a52 60%,#4d4a44 100%)}
.offer-badge{left:320px;top:136px;width:200px;height:200px;border-radius:50%;background:var(--badge);color:var(--white);text-align:center;padding-top:52px;font-family:"Oswald",Arial,sans-serif;font-style:italic;transform:rotate(-4deg)}
.offer-badge .big{font-size:40px;font-weight:700;line-height:42px;display:block}
.offer-badge .small{font-family:"Open Sans",Arial,sans-serif;font-size:18px;font-style:italic;letter-spacing:1px;display:block;margin-top:2px}
.slider-arrows{left:793px;top:464px;display:flex;gap:2px}
.slider-arrows span{width:24px;height:24px;background:var(--slider-btn);display:flex;align-items:center;justify-content:center}

/* upload band */
.upload-band{left:171px;top:696px;width:854px;height:140px;background:var(--brown-dark);padding:10px}
.upload-inner{width:100%;height:100%;border:1px solid #6a4f42;position:relative}
.upload-title{left:26px;top:18px;color:var(--white);font-weight:700;font-size:20px;white-space:nowrap}
.upload-title em{font-size:12px;font-weight:400;margin-left:10px;vertical-align:2px}
.upload-input{left:26px;top:61px;width:437px;height:36px;background:var(--white);border-radius:3px;font-size:10px;color:#9a948f;padding:12px 14px;text-transform:uppercase}
.btn{top:61px;height:36px;background:var(--tan);color:var(--white);font-size:12px;font-weight:700;text-transform:uppercase;display:flex;align-items:center;justify-content:center;border-radius:2px}
.btn-upload{left:470px;width:120px}
.btn-share{left:599px;width:214px}

/* intro */
.section-title{left:0;width:1200px;text-align:center;font-weight:700;font-size:19px;text-transform:uppercase;color:var(--ink)}
.intro-text{left:190px;width:820px;top:941px;text-align:center;font-family:Arial,sans-serif;font-size:14px;line-height:27px;color:var(--grey-text)}
.faint-rule{left:171px;top:1018px;width:854px;height:1px;background:linear-gradient(90deg,transparent,#ece8e4 30%,#ece8e4 70%,transparent)}

/* pricing */
.plan{top:1058px;width:256px;height:533px;border:1px solid var(--card-border);background:var(--card-bg);overflow:hidden}
.plan-head{height:128px;background:linear-gradient(#c0ad90,#a58e70);position:relative;text-align:center}
.plan-hours{height:30px;line-height:30px;background:var(--tan-light);color:#f7f1e8;font-size:14px}
.plan-name{font-weight:800;font-size:31px;line-height:34px;color:#8a7355;text-shadow:0 1px 0 #d9c9b0;padding-top:10px}
.ribbon{position:absolute;right:-34px;top:10px;width:120px;height:22px;background:var(--ribbon);color:var(--white);font-size:9px;font-weight:700;text-align:center;line-height:22px;transform:rotate(45deg);text-transform:uppercase}
.features{list-style:none;padding:8px 14px 0}
.features li{height:44px;border-bottom:1px solid #e6e2de;display:flex;align-items:center;font-family:Arial,sans-serif;font-size:11px;color:#6f6a66;gap:8px}
.features li::before{content:"+";width:14px;height:14px;border:1px solid #9b958f;border-radius:50%;font-size:12px;line-height:12px;text-align:center;color:#9b958f}
.plan-extra{text-align:center;font-size:22px;color:#6d6660;margin-top:16px}
.plan-price{text-align:center;font-size:27px;font-weight:700;color:var(--tan)}

.addons{left:0;width:1200px;top:1634px;text-align:center;font-weight:700;font-size:17px;text-transform:uppercase;color:var(--ink)}
.deposit{left:0;width:1200px;top:1664px;text-align:center;font-weight:700;font-size:22px;text-transform:uppercase;color:var(--tan-text)}

/* gallery */
.gallery-title{left:240px;width:720px;top:1735px;display:flex;align-items:center;gap:14px;font-weight:700;font-size:19px;text-transform:uppercase;white-space:nowrap}
.gallery-title .line{flex:1;height:1px;background:var(--ink)}
.gallery{left:171px;top:1801px;width:854px;height:527px;display:grid;grid-template-columns:repeat(4,1fr);grid-template-rows:repeat(3,1fr);gap:1px;background:#cfcfcf}
.tile{position:relative;filter:brightness(.62)}
.tile.active{filter:none}
.tile-caption{position:absolute;left:16px;top:126px;color:#111}
.tile-caption b{display:block;font-family:Arial,sans-serif;font-size:15px}
.tile-caption i{font-family:Arial,sans-serif;font-size:11px}

/* footer */
.footer-nav{left:0;width:1200px;top:2410px;display:flex;justify-content:center;gap:44px;font-size:11px;text-transform:uppercase}
.copyright{left:0;width:1200px;top:2442px;text-align:center;font-size:10px;text-transform:uppercase;color:#4a3f38}
.socials{left:0;width:1200px;top:2481px;display:flex;justify-content:center;gap:12px}
.socials span{width:42px;height:42px;border:1.5px solid #a9a4a0;border-radius:50%}
</style>
</head>
<body>

<header>
  <div class="abs brand"><span class="brand-dot"></span>Giggle Frames</div>
  <div class="abs double-rule" style="top:119px"></div>
  <nav class="abs main-nav">
    <span class="line"></span><span>Home</span><span class="sep">/</span><span>Pricing</span><span class="sep">/</span><span>Contact Us</span><span class="sep">/</span><span>Book an Event</span><span class="sep">/</span><span>Client Log In</span><span class="line"></span>
  </nav>
  <div class="abs double-rule" style="top:176px"></div>
</header>

<section class="abs hero">
  <div class="abs hero-photo-family" role="img" aria-label="Family of three posing together in a studio"></div>
  <div class="abs hero-photo-bike" role="img" aria-label="Young woman riding a bicycle in an autumn park"></div>
  <div class="abs offer-badge"><span class="big">WEEKEND<br>OFFER</span><span class="small">ALL WKND!</span></div>
  <div class="abs slider-arrows" style="left:792px;top:465px">
    <span><svg width="10" height="12" viewBox="0 0 10 12"><path d="M7 1 2 6l5 5" fill="none" stroke="#fff" stroke-width="1.6"/></svg></span>
    <span><svg width="10" height="12" viewBox="0 0 10 12"><path d="M3 1l5 5-5 5" fill="none" stroke="#fff" stroke-width="1.6"/></svg></span>
  </div>
</section>

<section class="abs upload-band">
  <div class="upload-inner">
    <div class="abs upload-title">UPLOAD YOUR LOVELY PICTURES<em>Lorem Ipsum is simply dummy text of the printing and typesetting industry.</em></div>
    <div class="abs upload-input">Share your photos</div>
    <div class="abs btn btn-upload">Upload</div>
    <div class="abs btn btn-share">Share picture galleries</div>
  </div>
</section>

<h2 class="abs section-title" style="top:867px">Giggle Frames Photo Booth</h2>
<div class="abs double-rule" style="top:912px"></div>
<p class="abs intro-text">We are a family owned and operated photo booth rental company serving Maplewood, Cedar Hollow, Ridgeford &amp; surrounding counties to create fun &amp; memorable memories for any type of event.</p>
<div class="abs faint-rule"></div>

<section>
  <article class="abs plan" style="left:171px">
    <div class="plan-head"><div class="plan-hours">3 hours of service</div><div class="plan-name">STANDARD<br>includes</div><div class="ribbon">Best Value</div></div>
    <ul class="features"><li>3 hours of service</li><li>Set up &amp; removal</li><li>Professional &amp; friendly booth attendant</li><li>DVD or usb flash drive of picture</li><li>Guestbook</li><li>Unlimited prints</li><li>Online gallery</li></ul>
    <div class="plan-extra">Digital backdrop</div><div class="plan-price">$675</div>
  </article>
  <article class="abs plan" style="left:468px">
    <div class="plan-head"><div class="plan-hours">4 hours of service</div><div class="plan-name">Ultimate<br>includes</div><div class="ribbon">Best Value</div></div>
    <ul class="features"><li>3 hours of service</li><li>Set up &amp; removal</li><li>Professional &amp; friendly booth attendant</li><li>DVD or usb flash drive of picture</li><li>Guestbook</li><li>Unlimited prints</li><li>Online gallery</li></ul>
    <div class="plan-extra">Digital backdrop</div><div class="plan-price">$850</div>
  </article>
  <article class="abs plan" style="left:764px">
    <div class="plan-head"><div class="plan-hours">5 hours of service</div><div class="plan-name">EXTREME<br>includes</div><div class="ribbon">Best Value</div></div>
    <ul class="features"><li>3 hours of service</li><li>Set up &amp; removal</li><li>Professional &amp; friendly booth attendant</li><li>DVD or usb flash drive of picture</li><li>Guestbook</li><li>Unlimited prints</li><li>Online gallery</li></ul>
    <div class="plan-extra">Digital backdrop</div><div class="plan-price">$975</div>
  </article>
</section>

<p class="abs addons">Add On's: Magnet photo strip frames, stand up acrylicphoto strip frames,</p>
<p class="abs deposit">Only $100 deposit</p>

<h2 class="abs gallery-title"><span class="line"></span>Picture Gallery<span class="line"></span></h2>
<section class="abs gallery">
  <div class="tile" role="img" aria-label="Family playing in a green field" style="background:linear-gradient(#9fb6c9,#6f8b3e)"></div>
  <div class="tile active" role="img" aria-label="Wedding couple in formal wear" style="background:linear-gradient(90deg,#d9d9d6 0%,#c9c6c1 48%,#e9837d 52%,#d86a66 100%)"><div class="tile-caption"><b>LOREM IPSUM</b><i>Click here for Enlarge</i></div></div>
  <div class="tile" role="img" aria-label="Black and white portrait of an elderly woman" style="background:linear-gradient(135deg,#2b2b2b,#8a8a8a,#1c1c1c)"></div>
  <div class="tile" role="img" aria-label="Smiling family of three" style="background:linear-gradient(135deg,#e9e4de,#c79a80)"></div>
  <div class="tile" role="img" aria-label="Family riding bicycles outdoors" style="background:linear-gradient(#6fa050,#3f6a35)"></div>
  <div class="tile" role="img" aria-label="Group of friends dancing" style="background:linear-gradient(135deg,#a6b0a9,#8c5d47)"></div>
  <div class="tile" role="img" aria-label="Portrait of a blonde woman" style="background:linear-gradient(135deg,#3a2c22,#b9925f,#2a2019)"></div>
  <div class="tile" role="img" aria-label="Mother and daughter laughing at the beach" style="background:linear-gradient(135deg,#c7d7e0,#c0805e)"></div>
  <div class="tile" role="img" aria-label="Happy family hugging" style="background:linear-gradient(135deg,#8fae5c,#d2a07e)"></div>
  <div class="tile" role="img" aria-label="Senior couple smiling" style="background:linear-gradient(135deg,#c8c5bf,#9c8878)"></div>
  <div class="tile" role="img" aria-label="Cyclist wearing a helmet" style="background:linear-gradient(135deg,#5c8a3a,#2f3a2a)"></div>
  <div class="tile" role="img" aria-label="Two friends in sunglasses smiling" style="background:linear-gradient(135deg,#a2c3d8,#d59a80)"></div>
</section>

<footer>
  <div class="abs double-rule" style="top:2379px"></div>
  <nav class="abs footer-nav"><span>Home</span><span>/</span><span>Pricing</span><span>/</span><span>Contact Us</span><span>/</span><span>Book an Event</span><span>/</span><span>Client Log In</span></nav>
  <p class="abs copyright">© Copyright. Giggle Frames. All rights reserved.</p>
  <div class="abs socials" aria-label="Social links"><span></span><span></span><span></span><span></span></div>
</footer>

</body>
</html>
```